Project Brightvale Wellness

We need a business/ logo card design for our company based out of Canada. We will be retailing cannibus products to our customers.
For colors I've found this online : https://www.huetrackr.example/palette-results/?colors=70ff02,ff0270,ff4a02,02e1ff . We especially like the green and blue .
We would like our business card design to communicate modern medicine .

Target Market(s)

males 20-40 years

Industry/Entity Type

Health And Wellness

Contact Information for Business Card

Address is : 248 Dunmore Ave E
Toronto, ON K7R 3T8
website: www.brightvalewellness.example

Font styles to use
Serif

Requirements
Must have
• clear, easy to read logo
Nice to have
• contrasting colors
Should not have
• we want to stay away from marijuana leaf

```html
<!DOCTYPE html>
<html lang="en">
<head>
<meta charset="utf-8">
<title>Brightvale Wellness — Business Card</title>
<link rel="stylesheet" href="https://fonts.googleapis.com/css2?family=Crimson+Text:wght@400;700&display=swap">
<style>
  :root {
    --page-bg: #eef1f3;
    --card-sky-top: #c9e9f8;
    --card-sky-mid: #a9dcf2;
    --card-sky-edge: #8fd0ee;
    --wave-pale: #bfe6f6;
    --wave-light: #8fd3ea;
    --wave-mid: #5cbcd9;
    --wave-deep: #3aa7c8;
    --wave-teal: #2b9bbd;
    --text-cream: #fbfbe6;
    --text-white: #ffffff;
    --brand-blue: #1b7fc4;
    --brand-green: #70c92a;
    --icon-tile: #e9f6ea;
  }
  * { box-sizing: border-box; margin: 0; padding: 0; }
  html, body {
    width: 1200px;
    height: 793px;
    overflow: hidden;
    background: var(--page-bg);
  }
  .canvas {
    position: relative;
    width: 1200px;
    height: 793px;
  }
  .business-card {
    position: absolute;
    left: 130px;
    top: 128px;
    width: 940px;
    height: 537px;
    border-radius: 26px;
    overflow: hidden;
    background:
      radial-gradient(ellipse at 78% 30%, rgba(255,255,255,0.55), rgba(255,255,255,0) 55%),
      radial-gradient(ellipse at 30% 15%, rgba(255,255,255,0.35), rgba(255,255,255,0) 45%),
      linear-gradient(180deg, var(--card-sky-top) 0%, var(--card-sky-mid) 55%, var(--card-sky-edge) 100%);
    box-shadow: 0 6px 18px rgba(40, 70, 90, 0.18);
  }
  .card-glow {
    position: absolute;
    inset: 0;
    background: radial-gradient(circle at 85% 20%, rgba(255,255,255,0.4), rgba(255,255,255,0) 40%);
  }
  .card-waves {
    position: absolute;
    left: 0;
    top: 0;
    width: 940px;
    height: 537px;
  }
  .address-block {
    position: absolute;
    left: 66px;
    top: 118px;
    font-family: "Crimson Text", Georgia, serif;
    color: var(--text-cream);
    font-size: 38px;
    line-height: 1.22;
    text-shadow: 0 1px 2px rgba(30, 90, 120, 0.35);
  }
  .home-icon {
    display: block;
    width: 40px;
    height: 40px;
    margin: 0 0 18px 92px;
  }
  .website {
    position: absolute;
    left: 40px;
    bottom: 40px;
    font-family: "Crimson Text", Georgia, serif;
    font-weight: 700;
    font-size: 34px;
    color: var(--text-white);
    text-shadow: 0 1px 2px rgba(20, 70, 100, 0.35);
  }
  .brand-mark {
    position: absolute;
    right: 46px;
    top: 78px;
    width: 300px;
    display: flex;
    flex-direction: column;
    align-items: center;
    gap: 16px;
  }
  .brand-dot {
    width: 46px;
    height: 46px;
    border-radius: 50%;
    background: var(--brand-green);
  }
  .brand-name {
    font-family: "Crimson Text", Georgia, serif;
    font-weight: 700;
    font-size: 44px;
    line-height: 1.05;
    text-align: center;
    color: var(--brand-blue);
  }
</style>
</head>
<body>
<main class="canvas">
  <section class="business-card" aria-label="Brightvale Wellness business card">
    <div class="card-glow"></div>

    <svg class="card-waves" viewBox="0 0 940 537" aria-hidden="true">
      <path d="M0 300 C 220 250, 420 300, 620 350 C 760 385, 860 400, 940 395 L940 537 L0 537 Z" fill="var(--wave-pale)" opacity="0.8"/>
      <path d="M0 335 C 200 300, 420 330, 600 380 C 740 418, 860 430, 940 425 L940 537 L0 537 Z" fill="var(--wave-light)"/>
      <path d="M0 375 C 180 345, 380 365, 560 410 C 720 448, 850 462, 940 458 L940 537 L0 537 Z" fill="var(--wave-mid)"/>
      <path d="M0 420 C 170 395, 360 410, 540 445 C 700 476, 840 492, 940 490 L940 537 L0 537 Z" fill="var(--wave-deep)"/>
      <path d="M0 470 C 160 452, 340 462, 520 485 C 680 505, 830 520, 940 520 L940 537 L0 537 Z" fill="var(--wave-teal)"/>
      <path d="M0 318 C 220 275, 430 318, 620 366 C 760 400, 860 414, 940 410" fill="none" stroke="#ffffff" stroke-opacity="0.55" stroke-width="2"/>
    </svg>

    <address class="address-block" style="font-style: normal;">
      <svg class="home-icon" viewBox="0 0 40 40" role="img" aria-label="Address">
        <rect x="1" y="1" width="38" height="38" rx="6" fill="var(--icon-tile)"/>
        <path d="M20 9 L32 20 L28.5 20 L28.5 31 L11.5 31 L11.5 20 L8 20 Z" fill="var(--brand-green)"/>
        <rect x="17" y="23" width="6" height="8" fill="var(--icon-tile)"/>
      </svg>
      <span class="address-line">248 Dunmore Ave E</span><br>
      <span class="address-line">Toronto, ON K7R 3T8</span>
    </address>

    <div class="brand-mark">
      <span class="brand-dot"></span>
      <span class="brand-name">Brightvale Wellness</span>
    </div>

    <p class="website">www.brightvalewellness.example</p>
  </section>
</main>
</body>
</html>
```